Concert Pianist Hot Foil Clear Plastic Business Card
Corveline-Hask Tonal Mgmt
Concert Pianist Hot Foil Clear Plastic Business Card - Music
Creative Brief
Use specific fonts
Use the font Freeky Typewriter (by Quillmarrow Type) for Corveline-Hask Tonal Mgmt. Use a standard fo
Cutting-Edge
Dorian Felsk
Corveline_hask Tonal Mgmt
27816 Old Quarry Road Suite 418 Halvenport, Ostmark 40217
DorianFelsk@Mirelodan.example
www.Mirelodan.example
We like this card and would recommend it as a model. http://www.lucentprintworks.example/glasshue/images/businesscards/clearcard4.jpg Here are pictures that can be used: http://s204.beta.snapvaultly.example/user/daedalwander/library/Mirelodan%20Business%20Card? We want the web site to be the most distinctive address.
Nothing on the back is required but--if you are cleaver you can place a photograph behind picture on front. You can chose from the selection provided. (All of the pictures are recent except for the B & W photograph with bow tie.) http://s204.beta.snapvaultly.example/user/daedalwander/library/Mirelodan%20Business%20Card?

```html
<!DOCTYPE html>
<html lang="en">
<head>
<meta charset="utf-8">
<title>Corveline-Hask Tonal Mgmt – Business Card</title>
<link rel="stylesheet" href="https://fonts.googleapis.com/css2?family=Special+Elite&family=Archivo+Narrow:wght@400;600&family=Questrial&display=swap">
<style>
  :root {
    --backdrop: #1b1714;
    --card-smoke: #5a5550;
    --card-smoke-dark: #3a3633;
    --foil-gold: #c6a766;
    --foil-gold-light: #dcc48f;
    --ink-dark: #1e1b18;
    --silver: #d8d6d2;
    --photo-top: #6d5a48;
    --photo-bottom: #2a221d;
  }
  * { box-sizing: border-box; margin: 0; padding: 0; }
  html, body {
    width: 1200px; height: 600px; overflow: hidden;
    background: var(--backdrop);
  }
  .canvas {
    position: relative; width: 1200px; height: 600px;
    display: flex; justify-content: center; align-items: center; gap: 50px;
  }
  .card {
    position: relative; width: 520px; height: 300px; overflow: hidden;
    border-radius: 4px;
    background: linear-gradient(180deg, var(--card-smoke), var(--card-smoke-dark));
    box-shadow: 0 10px 30px rgba(0,0,0,.5);
  }
  .card-swoosh { position: absolute; inset: 0; width: 100%; height: 100%; }

  /* Contact card */
  .agency-name {
    position: absolute; top: 24px; right: 24px;
    font-family: "Special Elite", "Courier New", monospace;
    font-weight: 400; font-size: 24px; color: var(--ink-dark);
    white-space: nowrap;
  }
  .contact {
    position: absolute; top: 94px; right: 24px; text-align: right;
    font-family: "Archivo Narrow", sans-serif; color: var(--ink-dark);
    font-size: 14px; line-height: 1.4;
  }
  .contact .person { font-size: 16px; font-weight: 400; margin-bottom: 2px; }
  .contact .line { display: block; white-space: nowrap; }
  .contact .email { margin-top: 22px; font-weight: 600; }
  .show-through {
    position: absolute; left: 22px; bottom: 24px;
    transform: rotate(180deg);
    font-family: "Questrial", sans-serif; color: rgba(60,55,50,.55);
    line-height: 1;
  }
  .show-through .first { font-size: 24px; letter-spacing: 1px; }
  .show-through .last { font-size: 34px; letter-spacing: 2px; font-weight: 700; }

  /* Artist card */
  .artist-photo {
    position: absolute; left: 0; top: 0; width: 215px; height: 100%;
    background: linear-gradient(160deg, var(--photo-top), var(--photo-bottom));
  }
  .artist-name {
    position: absolute; right: 28px; top: 150px; text-align: right;
    font-family: "Questrial", sans-serif; font-weight: 400; line-height: 1;
  }
  .artist-name .first { display: block; font-size: 36px; letter-spacing: 1px; color: var(--silver); }
  .artist-name .last { display: block; font-size: 36px; letter-spacing: 2px; margin-top: 4px; font-weight: 700; color: var(--ink-dark); }
  .artist-site {
    position: absolute; right: 70px; bottom: 24px;
    font-family: "Archivo Narrow", sans-serif; font-size: 14px; color: #fff;
  }
</style>
</head>
<body>
<main class="canvas">
  <section class="card card-contact">
    <svg class="card-swoosh" viewBox="0 0 520 300" preserveAspectRatio="none" aria-hidden="true">
      <path d="M200 0 H520 V300 H0 V170 C90 150 150 90 200 0 Z" fill="var(--foil-gold)" opacity=".85"/>
      <path d="M215 0 C175 100 110 165 0 190" fill="none" stroke="var(--foil-gold-light)" stroke-width="2"/>
    </svg>
    <h1 class="agency-name">Corveline-Hask Tonal Mgmt</h1>
    <div class="contact">
      <p class="person">Dorian Felsk</p>
      <p class="phone">374 555-0148</p>
      <p class="address">
        <span class="line">27816 Old Quarry Road Suite 418</span>
        <span class="line">Halvenport, Ostmark 40217</span>
      </p>
      <p class="email">DorianFelsk@Mirelodan.example</p>
    </div>
    <div class="show-through" aria-hidden="true">
      <div class="last">CORVELINE</div>
      <div class="first">MIRELODAN</div>
    </div>
  </section>

  <section class="card card-artist">
    <div class="artist-photo" role="img" aria-label="Photograph of the pianist in a dark suit standing beside a grand piano"></div>
    <svg class="card-swoosh" viewBox="0 0 520 300" preserveAspectRatio="none" aria-hidden="true">
      <path d="M215 300 C300 240 420 230 520 260 V300 Z" fill="var(--foil-gold)" opacity=".55"/>
    </svg>
    <h2 class="artist-name">
      <span class="first">MIRELODAN</span>
      <span class="last">CORVELINE</span>
    </h2>
    <p class="artist-site">www.Mirelodan.example</p>
  </section>
</main>
</body>
</html>
```